Menu Design Project for New Catering company

I would like to see my menus in a warm, inviting format. I prepare food for small intimate dinners, business lunches, picnics, parties, weddings and rehearsal dinners. I work with clients to help create their dream whether it includes items on my menu or to prepare very personal dishes that bring them warm memories of a special time or moment.

Target Market(s)

Organizations, wedding and or event planners

Industry/Entity Type

Catering

Requirements
Must have
• I would like to include the logo that is included in the attachment below. I also included a copy of the poster Lio Brenn created for me. I hope this helps. Please be creative. I am a very happy, cheerful person that enjoys cooking and having fun. I would like the design to represent my personality as well as my food. When I cater I treat my customers like an extension of my family and it comes across to them with everything I do for them. I hope this can somehow be reflected in your designs.
Should not have
• I'm open to all ideas and don't want to limit your creativity.

```html
<!DOCTYPE html>
<html lang="en">
<head>
<meta charset="utf-8">
<title>Boxed Lunch Menu Options – Warm Basil Catering</title>
<link rel="stylesheet" href="https://fonts.googleapis.com/css2?family=Raleway:wght@400;600;700&family=Crimson+Text:wght@400&display=swap">
<style>
  :root {
    --green: #1b8b3f;
    --heading-grey: #4a4a4a;
    --body-grey: #444444;
    --tan: #b8946a;
    --panel: #ebe4dc;
    --dots: #b8946a;
    --paper: #ffffff;
  }
  html, body { margin: 0; padding: 0; overflow: hidden; background: var(--paper); }
  .menu {
    position: relative;
    width: 934px;
    height: 1200px;
    overflow: hidden;
    background: var(--paper);
    font-family: "Raleway", sans-serif;
    color: var(--body-grey);
  }
  .menu-title {
    position: absolute; top: 62px; left: 0; width: 100%;
    margin: 0; text-align: center; line-height: 30px;
    font-family: "Raleway", sans-serif; font-weight: 700;
    font-size: 24.5px; letter-spacing: 0.6px; color: var(--heading-grey);
  }
  .pricing {
    position: absolute; top: 110px; left: 0; width: 934px;
    margin: 0; text-align: center; white-space: nowrap;
    font-family: "Crimson Text", serif; font-size: 22.2px; line-height: 23.5px;
    letter-spacing: -0.5px; color: var(--green);
  }
  .ordering-note {
    position: absolute; top: 188px; left: 0; width: 934px;
    margin: 0; text-align: center; white-space: nowrap;
    font-size: 13.2px; line-height: 16px; color: var(--tan);
  }
  .hero-photo {
    position: absolute; top: 275px; left: 118px; width: 696px; height: 171px;
    background:
      radial-gradient(ellipse 22% 60% at 55% 45%, #c8743a 0%, rgba(200,116,58,0) 100%),
      radial-gradient(ellipse 40% 70% at 55% 55%, #4f8a2e 0%, rgba(79,138,46,0) 100%),
      linear-gradient(90deg, #d2453f 0%, #e9e4e0 10%, #f2f0ee 22%, #6a9a3d 40%, #c66a34 55%, #5c8f32 70%, #efedea 88%, #e4a3a6 100%);
  }
  .dishes {
    position: absolute; top: 470px; left: 0; width: 934px;
    margin: 0; padding: 0; list-style: none; text-align: center;
  }
  .dish { padding-bottom: 24px; }
  .dish-name {
    margin: 0; font-weight: 400; font-size: 19px; letter-spacing: 0.4px;
    color: var(--green); line-height: 22px;
  }
  .dish-desc {
    margin: 0; white-space: nowrap; font-size: 13.6px; line-height: 16px; color: var(--body-grey);
  }
  .extras-panel {
    position: absolute; top: 943px; left: 118px; width: 253px; height: 178px;
    background: var(--panel); text-align: center;
  }
  .extras-title {
    margin: 12px 0 0; font-weight: 400; font-size: 19px; line-height: 23px;
    letter-spacing: 0.4px; color: var(--green);
  }
  .extras-text { margin: 7px 0 0; font-size: 13.6px; line-height: 16px; color: var(--body-grey); }
  .dotted-rule {
    margin: 10px auto 0; width: 186px; border: 0; border-top: 3px dotted var(--dots); height: 0;
  }
  .brand {
    position: absolute; top: 1018px; left: 568px; width: 260px; text-align: center;
  }
  .brand-name {
    margin: 0; font-weight: 600; font-size: 22px; line-height: 28px; color: var(--green);
  }
  .contact {
    margin: 29px 0 0; font-size: 13.6px; line-height: 15.6px; color: var(--green);
  }
</style>
</head>
<body>
<main class="menu">
  <h1 class="menu-title">– BOXED LUNCH MENU OPTIONS –</h1>

  <p class="pricing">BOX LUNCHES – &nbsp;$10.00 Each, Served with chips, choice of fruit cup or side salad,<br>also included choice of cookie or cupcake. Drinks sold separately.<br>NOTE: &nbsp;A delivery fee of $20.00 will be assessed for orders totaling less than $150.00</p>

  <p class="ordering-note">Please send your order to my e-mail address at least 24 Hours in advance also include time requested,<br>address and contact information (including phone number) - I will send you a confirmation that the order has<br>been received and invoiced day of delivery.</p>

  <div class="hero-photo" role="img" aria-label="Photo of a grilled chicken breast on a spinach and chickpea salad with tomatoes, fork and knife on a red floral tablecloth"></div>

  <ul class="dishes">
    <li class="dish">
      <h2 class="dish-name">MALIBU CHICKEN</h2>
      <p class="dish-desc">Grilled chicken breast, topped with sweet honey baked ham, Swiss cheese and served on a fresh croissant<br>with a side of rich sweet mustard sauce</p>
    </li>
    <li class="dish">
      <h2 class="dish-name">ITALIAN MEATBALL WITH MOZZARELLA CHEESE</h2>
      <p class="dish-desc">in a rich marinara sauce served on a fresh Hoagie Bun</p>
    </li>
    <li class="dish">
      <h2 class="dish-name">GRILLED HAWAIIAN CHICKEN SANDWICH</h2>
      <p class="dish-desc">Grilled chicken topped with a sweet grilled pineapple ring and guacamole sauce on a fresh Hawaiian bun or<br>croissant</p>
    </li>
    <li class="dish">
      <h2 class="dish-name">HONEY CHICKEN SALAD</h2>
      <p class="dish-desc">A fresh chicken salad filled with grapes, crispy celery, pecans, shredded chicken - served on a fresh croissant</p>
    </li>
    <li class="dish">
      <h2 class="dish-name">HONEY BAKED HAM AND SWISS CHEESE</h2>
      <p class="dish-desc">piled high on a fresh croissant (with choices of - lettuce, tomato slice, onions and mayo/salad dressing)</p>
    </li>
    <li class="dish">
      <h2 class="dish-name">ULTIMATE BLT WITH AVOCADO AND SPICY MAYO</h2>
      <p class="dish-desc">Crispy bacon, lettuce, tomato, thin slices of red onion, avocado slices atop toasted bread with spicy mayo.</p>
    </li>
    <li class="dish">
      <h2 class="dish-name">SPINACH SALAD WITH BACON DRESSING</h2>
      <p class="dish-desc">Baby Spinach, mushrooms, red onions and sliced boiled eggs served with croissant and bacon dressing.</p>
    </li>
  </ul>

  <aside class="extras-panel">
    <h3 class="extras-title">SALAD DRESSING<br>CHOICES</h3>
    <p class="extras-text">Ranch, Italian, Honey Mustard<br>or Blue Cheese</p>
    <hr class="dotted-rule">
    <p class="extras-text">Drinks - 12 oz. soft drinks or 16<br>oz. bottled water- $1.00 each</p>
  </aside>

  <footer class="brand">
    <p class="brand-name">Warm Basil Catering</p>
    <p class="contact">www.warmbasilcatering.com<br>555-014-2736<br>Nora@warmbasilcatering.com</p>
  </footer>
</main>
</body>
</html>
```